TWR Business Card Design

As a full service media and advocacy firm, we lean on years of experience in political and corporate consulting, grassroots campaigning, media placement, and video production to deliver unparalleled results. Recently we have moved into digital media and now provide this service for our clients.

I will add our two company logos to be used on the business cards. The longer logo with "sky reach studio" is our primary logo. Our secondary logo is more square one with "sky reach" and 'digital.media.campaigns" on it. We are looking for clean and modern looking business cards fitting for a digital firm.

I will also add our logos that go well with dark backgrounds.

Industry/Entity Type

Political

Contact Information for Business Card

Walter Pennick, Director of Campaigns and Digital, 555-218-4760, walter@skyreachstudioco.example, @SkyReachStudioCo, @WalterPennick, Facebook.com/SkyReachStudioCo

```html
<!DOCTYPE html>
<html lang="en">
<head>
<meta charset="utf-8">
<title>TWR Business Card</title>
<link href="https://fonts.googleapis.com/css2?family=Cabin:wght@400;500;700&display=swap" rel="stylesheet">
<style>
  :root {
    --navy: #13398f;
    --sky: #2a8fdb;
    --ink: #1a2a55;
    --paper: #ffffff;
    --backdrop: #e6e8ec;
  }
  html, body {
    margin: 0;
    width: 1200px;
    height: 898px;
    overflow: hidden;
    background: var(--backdrop);
    font-family: "Cabin", sans-serif;
  }
  .card {
    position: absolute;
    left: 150px;
    top: 192px;
    width: 900px;
    height: 514px;
    background: var(--paper);
    box-shadow: 0 6px 24px rgba(0,0,0,0.18);
    overflow: hidden;
  }
  .band { position: absolute; left: 0; right: 0; background: var(--navy); }
  .band--top-edge { top: 0; height: 14px; }
  .band--top-inner { top: 24px; height: 16px; }
  .band--bottom-inner { bottom: 30px; height: 22px; }
  .band--bottom-edge { bottom: 0; height: 18px; }

  .brand {
    position: absolute;
    left: 40px;
    top: 230px;
    width: 340px;
    display: flex;
    align-items: center;
    justify-content: center;
    gap: 14px;
  }
  .brand__dot {
    width: 18px; height: 18px;
    border-radius: 50%;
    background: var(--sky);
  }
  .brand__name {
    font-size: 52px;
    font-weight: 700;
    color: var(--navy);
    letter-spacing: 1px;
    text-transform: uppercase;
    line-height: 1;
  }

  .divider {
    position: absolute;
    left: 420px;
    top: 95px;
    width: 5px;
    height: 335px;
    background: var(--navy);
  }

  .contact {
    position: absolute;
    left: 450px;
    top: 92px;
    color: var(--ink);
  }
  .contact__name {
    margin: 0;
    font-size: 34px;
    font-weight: 700;
    color: var(--navy);
    letter-spacing: 0.5px;
  }
  .contact__title {
    margin: 4px 0 10px;
    font-size: 21px;
    line-height: 1.2;
    color: var(--sky);
  }
  .contact__list { list-style: none; margin: 0; padding: 0; }
  .contact__item {
    display: flex;
    align-items: baseline;
    font-size: 23px;
    line-height: 1.38;
  }
  .contact__label {
    width: 24px;
    font-size: 10px;
    font-weight: 700;
    color: var(--navy);
  }
</style>
</head>
<body>
  <div class="card">
    <div class="band band--top-edge"></div>
    <div class="band band--top-inner"></div>

    <div class="brand">
      <span class="brand__name">sky reach</span>
      <span class="brand__dot"></span>
    </div>

    <div class="divider"></div>

    <div class="contact">
      <h1 class="contact__name">Walter Pennick</h1>
      <p class="contact__title">Director of<br>Campaigns and Digital</p>
      <ul class="contact__list">
        <li class="contact__item"><span class="contact__label">M</span>555-218-4760</li>
        <li class="contact__item"><span class="contact__label">E</span>walter@skyreachstudioco.example</li>
        <li class="contact__item"><span class="contact__label">I</span>@SkyReachStudioCo</li>
        <li class="contact__item"><span class="contact__label">T</span>@WalterPennick</li>
        <li class="contact__item"><span class="contact__label">F</span>/SkyReachStudioCo</li>
      </ul>
    </div>

    <div class="band band--bottom-inner"></div>
    <div class="band band--bottom-edge"></div>
  </div>
</body>
</html>
```